" A RotaBem é uma empresa que oferece soluçoes de TI online específico para empresas que comercializam benefícios como, Vale alimentaçao, refeiçao e Transporte. "

```html
<!DOCTYPE html>
<html lang="pt-BR">
<head>
<meta charset="utf-8">
<title>RotaBem – cartão de visita</title>
<link rel="stylesheet" href="https://fonts.googleapis.com/css2?family=Ubuntu:wght@400;500;700&display=swap">
<style>
  :root {
    --bg: #ececec;
    --card: #ffffff;
    --blue: #1f8ad9;
    --grey: #8c8f92;
    --grey-dark: #5e6266;
    --grey-band: #9a9da0;
    --text: #6a6e72;
    --navy: #1f4e79;
  }
  * { box-sizing: border-box; margin: 0; padding: 0; }
  html, body { width: 1200px; height: 1200px; overflow: hidden; }
  body { background: var(--bg); font-family: "Ubuntu", sans-serif; position: relative; }

  .card { position: absolute; background: var(--card); overflow: hidden; }

  /* front */
  .card-front { left: 72px; top: 60px; width: 888px; height: 497px; }
  .front-brand {
    position: absolute; left: 240px; top: 196px;
    font-size: 78px; font-weight: 700; color: var(--grey); letter-spacing: 1px;
  }
  .front-tagline {
    position: absolute; left: 498px; top: 294px;
    font-size: 26px; color: var(--grey); letter-spacing: 0.5px;
  }
  .group-mark { position: absolute; left: 60px; top: 418px; display: flex; align-items: center; gap: 10px; }
  .group-mark .square { width: 44px; height: 44px; background: var(--navy); }
  .group-mark .label { color: var(--navy); font-weight: 700; font-size: 22px; line-height: 1; }
  .group-mark .label small { display: block; font-size: 10px; font-weight: 400; letter-spacing: 4px; margin-top: 4px; }

  /* back */
  .card-back { left: 216px; top: 622px; width: 895px; height: 502px; }
  .band-top { position: absolute; left: 0; top: 0; width: 100%; height: 156px; background: var(--blue); }
  .band-top .back-brand {
    position: absolute; left: 0; right: 0; top: 52px; text-align: center;
    color: #fff; font-weight: 700; font-size: 50px; letter-spacing: 1px;
  }
  .band-bottom { position: absolute; left: 0; bottom: 0; width: 100%; height: 60px; background: var(--blue); }

  .name-tag {
    position: absolute; left: 0; top: 262px; width: 276px; height: 84px;
    background: var(--grey-band); color: #fff; text-align: right; padding: 12px 22px 0 0;
  }
  .name-tag .name { font-weight: 700; font-size: 30px; letter-spacing: 0.5px; }
  .name-tag .role { font-size: 18px; letter-spacing: 1px; margin-top: 4px; }
  .edge-block { position: absolute; right: 0; top: 262px; width: 57px; height: 84px; background: var(--grey-band); }
  .divider { position: absolute; left: 276px; top: 222px; width: 2px; height: 160px; background: #d6d7d8; }

  .contact-list { position: absolute; left: 316px; top: 226px; list-style: none; }
  .contact-list li { display: flex; align-items: center; gap: 14px; height: 39px; font-size: 21px; color: var(--text); }
  .contact-list svg { width: 28px; height: 28px; flex: none; }
  .contact-list .site { font-size: 27px; color: var(--grey-dark); }
  .contact-list .site b { font-weight: 700; }
</style>
</head>
<body>

<section class="card card-front">
  <div class="front-brand">RotaBem</div>
  <div class="front-tagline">to benefits</div>
  <div class="group-mark">
    <div class="square"></div>
    <div class="label">GRUPO QUINTEC<small>tecnologia</small></div>
  </div>
</section>

<section class="card card-back">
  <div class="band-top"><div class="back-brand">RotaBem</div></div>

  <div class="name-tag">
    <div class="name">MARCOS LIMA</div>
    <div class="role">DIRETOR</div>
  </div>
  <div class="divider"></div>
  <div class="edge-block"></div>

  <ul class="contact-list">
    <li>
      <svg viewBox="0 0 28 28"><circle cx="14" cy="14" r="14" fill="#8c8f92"/><rect x="10" y="7" width="8" height="14" rx="1.5" fill="#fff"/><rect x="11.5" y="9" width="5" height="8" fill="#8c8f92"/></svg>
      00 0000-0000 / 0000-0000
    </li>
    <li>
      <svg viewBox="0 0 28 28"><circle cx="14" cy="14" r="14" fill="#8c8f92"/><rect x="7" y="9" width="14" height="10" rx="1" fill="#fff"/><path d="M7 9 L14 15 L21 9" fill="none" stroke="#8c8f92" stroke-width="1.5"/></svg>
      contato@rotabem.com.br
    </li>
    <li>
      <svg viewBox="0 0 28 28"><circle cx="14" cy="14" r="14" fill="#8c8f92"/><path d="M14 6a5.5 5.5 0 0 0-5.5 5.5C8.5 16 14 22 14 22s5.5-6 5.5-10.5A5.5 5.5 0 0 0 14 6z" fill="#fff"/><circle cx="14" cy="11.5" r="2" fill="#8c8f92"/></svg>
      Tv. Aurora dos Campos, 00 - Vila Nova - SP
    </li>
    <li class="site">
      <svg viewBox="0 0 28 28"><circle cx="14" cy="14" r="14" fill="#8c8f92"/><g fill="none" stroke="#fff" stroke-width="1.5"><circle cx="14" cy="14" r="7"/><ellipse cx="14" cy="14" rx="3" ry="7"/><line x1="7" y1="14" x2="21" y2="14"/></g></svg>
      <span><b>ROTABEM</b>.COM.BR</span>
    </li>
  </ul>

  <div class="band-bottom"></div>
</section>

</body>
</html>
```